SOS! The Thistle cafe is in need of a menu face lift!

We need a standout looking menu for our evolving cafe. Our business has grown greatly from our fresh and changing menu, however the menu (look) itself isn't inspiring and is basic.
I have attached some photos of the business and menus I like the look of.
I am open to other ideas (this is why I need your creative help)
Our menu is currently on an A5 clip board, however we are willing to change it a different size if needed.

Would love to have it a multi function eg, used as a takeaway menu as well, possibly bi-fold? Added Wednesday, June 8, 2016

• It would be cool to have some old sea/ pirate references?

```html
<!DOCTYPE html>
<html lang="en">
<head>
<meta charset="utf-8">
<title>The Thistle Cafe Menu</title>
<link href="https://fonts.googleapis.com/css2?family=Bebas+Neue&family=Architects+Daughter&display=swap" rel="stylesheet">
<style>
:root{
  --backdrop:#e6e2dc;
  --kraft:#c6a87e;
  --kraft-dark:#b39469;
  --ink:#2a231d;
  --ink-soft:#4a3f34;
  --rule:#6b5b49;
}
*{box-sizing:border-box;margin:0;padding:0}
html,body{width:1200px;height:841px;overflow:hidden;background:var(--backdrop)}
body{position:relative;font-family:"Architects Daughter",cursive;color:var(--ink)}
.panel{position:absolute;top:16px;height:809px;background:var(--kraft);box-shadow:0 2px 6px rgba(0,0,0,.18)}
.cover{left:16px;width:260px}
.back{left:292px;width:292px;padding:14px 16px}
.spread{left:600px;width:584px;display:flex}
.chain{position:absolute;top:0;bottom:0;border-left:3px dotted var(--ink)}
.cover .chain.left{left:16px}
.cover .chain.right{right:16px}

.wordmark{position:absolute;left:0;right:0;text-align:center;color:var(--ink)}
.cover .wordmark{top:560px}
.wordmark-name{font-family:"Bebas Neue",sans-serif;font-weight:400;font-size:40px;line-height:1;display:inline-flex;align-items:center;gap:8px}
.wordmark-dot{display:inline-block;width:12px;height:12px;background:var(--ink)}
.wordmark-tag{font-family:"Architects Daughter",cursive;font-size:13px;margin-top:4px}

.section-title{font-family:"Bebas Neue",sans-serif;font-size:19px;letter-spacing:1px;text-align:center;line-height:1;margin:4px 0 2px}
.dash-rule{border-top:2px dashed var(--ink);margin:4px 0}
.item{margin-bottom:5px}
.row{display:flex;justify-content:space-between;align-items:baseline;font-size:10px;text-transform:uppercase;line-height:1.2}
.row .price{font-size:9.5px}
.desc{font-size:7.5px;line-height:1.25;color:var(--ink-soft);text-transform:uppercase}
.desc.lower{text-transform:none;font-size:8px}

.drinks-band{background:var(--kraft-dark);margin:8px -16px 6px;padding:4px 16px;font-family:"Bebas Neue",sans-serif;font-size:26px;letter-spacing:1px}
.drinks-grid{display:flex;gap:8px}
.hot{flex:1.25}
.cold{flex:1;border-left:2px dashed var(--ink);padding-left:7px}
.cups{display:flex;gap:8px;margin:4px 0;font-size:8.5px;text-align:center}
.cups svg{display:block;margin:0 auto}
.mini{font-size:8.5px;line-height:1.3;text-transform:uppercase}
.mini .r{display:flex;justify-content:space-between}
.sub-title{font-family:"Bebas Neue",sans-serif;font-size:15px;line-height:1;margin:3px 0 2px}
.fold{position:absolute;left:0;right:0;top:530px;border-top:3px dotted var(--ink)}
.back .wordmark{top:660px}
.back .wordmark-name{font-size:32px}

.col{position:relative;width:292px;padding:12px 14px}
.col + .col{border-left:3px dotted var(--ink)}
.menu-head{display:flex;justify-content:space-between;align-items:flex-end;background:var(--kraft-dark);margin:0 -14px 8px;padding:6px 14px 4px}
.menu-head h2{font-family:"Bebas Neue",sans-serif;font-size:30px;font-weight:400;line-height:1;letter-spacing:.5px}
.menu-head .when{font-family:"Bebas Neue",sans-serif;font-size:12px;line-height:1.05;text-align:right}
.col .item{border-bottom:1px solid var(--rule);padding-bottom:2px;margin-bottom:5px}
.col .item.plain{border-bottom:0}
.group-title{font-family:"Bebas Neue",sans-serif;font-size:17px;text-align:center;line-height:1;margin:8px 0 1px}
.group-note{font-size:7px;text-align:center;text-transform:uppercase;color:var(--ink-soft);margin-bottom:5px}
.extras{font-size:8.5px;line-height:1.35}
.extras .label{text-align:center;font-size:9.5px;text-transform:uppercase;margin:6px 0 3px}
.vegan{font-size:9px;text-align:center;text-decoration:underline;margin-top:8px}
</style>
</head>
<body>

<section class="panel cover">
  <div class="chain left"></div>
  <div class="chain right"></div>
  <div class="wordmark">
    <div class="wordmark-name"><span class="wordmark-dot"></span>The Thistle</div>
    <div class="wordmark-tag">cafe &amp; kitchen</div>
  </div>
</section>

<section class="panel back">
  <h3 class="section-title">Salads</h3>
  <div class="dash-rule"></div>
  <div class="item"><div class="row"><span>Chicken Caesar</span><span class="price">$17.5</span></div>
    <div class="desc">grilled chicken, bacon, mixed lettuce, parmesan cheese, croutons, caesar dressing topped with a poached egg</div></div>
  <div class="item"><div class="row"><span>Prawn &amp; Avocado</span><span class="price">$18.5</span></div>
    <div class="desc">lettuce, tomato, spanish onion, capsicum, grilled prawns w/ thousand island dressing &amp; fresh avocado</div></div>
  <div class="item"><div class="row"><span>Ranch</span><span class="price">$18.5</span></div>
    <div class="desc">chicken schnitzel, bacon, mixed lettuce, tomato, carrot, capsicum, beetroot, spanish onion, parmesan w/ ranch dressing</div></div>

  <h3 class="section-title">Sandwiches</h3>
  <div class="dash-rule"></div>
  <div class="row"><span>Fresh $6.0 / Toasted $6.5</span><span class="price">for 3 fillings</span></div>
  <div class="mini" style="margin-top:3px">
    <div class="r"><span>Hawaiian</span><span>leg ham, cheese &amp; pineapple</span></div>
    <div class="r"><span>Tropical</span><span>chicken, cheese &amp; pineapple</span></div>
    <div class="r"><span>HCT</span><span>leg ham, cheese &amp; tomato</span></div>
  </div>

  <div class="drinks-band">Drinks</div>
  <div class="drinks-grid">
    <div class="hot">
      <div class="sub-title">Hot Drinks</div>
      <div class="cups">
        <div><svg width="16" height="16" viewBox="0 0 16 16"><path d="M2 4h10v7a3 3 0 0 1-3 3H5a3 3 0 0 1-3-3z" fill="none" stroke="#2a231d" stroke-width="1.4"/></svg>CUP<br>$3.5</div>
        <div><svg width="18" height="18" viewBox="0 0 18 18"><path d="M2 3h10v11H2z M12 6h3v5h-3" fill="none" stroke="#2a231d" stroke-width="1.4"/></svg>MUG<br>$4.5</div>
        <div><svg width="18" height="20" viewBox="0 0 18 20"><path d="M2 2h10v16H2z M12 6h3v6h-3" fill="none" stroke="#2a231d" stroke-width="1.4"/></svg>XL<br>$5.5</div>
      </div>
      <div class="mini">
        <div>Espresso <span style="float:right">$2.5</span></div>
        <div>Long Black</div><div>Cappuccino</div><div>Latte</div><div>Mocha</div><div>Chocolate</div><div>Choc Mint</div><div>Choc Chilli</div><div>White Chocchai</div><div>Vanilla Chai</div>
        <div style="margin-top:3px">Extras</div>
        <div class="r"><span>coffee shot</span><span>+$0.5</span></div>
        <div class="r"><span>syrup</span><span>+$0.5</span></div>
        <div class="r"><span>honey</span><span>+$0.5</span></div>
        <div class="r"><span>soy milk cup / mug / xl</span><span>+$0.5</span></div>
      </div>
    </div>
    <div class="cold">
      <div class="sub-title">Tea Tonics</div>
      <div class="mini">
        <div>2 cup pot $4.5</div>
        <div>-english breakfast</div><div>-earl grey</div><div>-well-being</div><div>-coconut tea</div><div>-berry green</div><div>-chai tea</div><div>-green tea</div><div>-peppermint</div><div>-g.l.e.w tea</div><div>&amp; white tea</div>
      </div>
      <div class="sub-title" style="margin-top:6px">Cans $2.5</div>
      <div class="mini">
        <div>make it a spider +$1.5</div>
        <div>harbour cola / diet</div><div>cola zero /</div><div>lemonade / zesta /</div><div>orange /</div><div>creaming soda</div>
      </div>
    </div>
  </div>

  <div class="fold"></div>
  <div class="wordmark">
    <div class="wordmark-name"><span class="wordmark-dot"></span>The Thistle</div>
    <div class="wordmark-tag">cafe &amp; kitchen</div>
  </div>
</section>

<section class="panel spread">
  <div class="col breakfast">
    <header class="menu-head"><h2>Breakfast Menu</h2><div class="when">All Day</div></header>
    <div class="item"><div class="row"><span>Toast</span><span class="price">served buttered</span></div>
      <div class="row"><span>2 slices</span><span class="price">$4.5</span></div>
      <div class="desc lower">sourdough white or wholemeal, block white or wholemeal, or turkish. jam, yeast spread, honey, peanut butter or cinnamon sugar +$0.5</div></div>
    <div class="item"><div class="row"><span>GF Bread (2)</span><span class="price">$5.5</span></div></div>
    <div class="item"><div class="row"><span>Turkish Raisin (2) Toast</span><span class="price">$5.5</span></div></div>
    <div class="item"><div class="row"><span>Banana Bread (GF)</span><span class="price">$5.5</span></div>
      <div class="desc">add whipped mascarpone w/ honey +$2.5</div></div>
    <div class="item"><div class="row"><span>Granola Muesli</span><span class="price">$12.5</span></div>
      <div class="desc">home made with yoghurt &amp; our own berry compote</div></div>
    <div class="item"><div class="row"><span>Spanish Eggs</span><span class="price">$12.5 / $14.5</span></div>
      <div class="desc lower">w/ parmesan cheese with toasted sourdough, w/ chorizo. two poached eggs in a warm spanish tomato salsa</div></div>
    <div class="item"><div class="row"><span>Bacon &amp; Eggs</span><span class="price">$13.5</span></div>
      <div class="desc">poached / scrambled or fried on sourdough toast &amp; side of relish</div></div>
    <div class="item"><div class="row"><span>Bacon &amp; Egg Sandwich</span><span class="price">$9.0</span></div>
      <div class="desc">turkish bread lightly toasted with (2) bacon, fried egg &amp; your choice of house relish / hollandaise / bbq sauce</div></div>
    <div class="item"><div class="row"><span>Lifestyle Breakfast</span><span class="price">$17.5</span></div>
      <div class="desc">wholemeal sourdough topped with wilted baby spinach, asparagus, mushrooms, two poached eggs w/ grilled tomato &amp; fresh avocado</div></div>
    <div class="item"><div class="row"><span>Eggs Benedict toasted sourdough</span><span class="price">$12.5</span></div>
      <div class="mini" style="font-size:8px">
        <div class="r"><span>w baby spinach, poached eggs &amp; hollandaise</span><span></span></div>
        <div class="r"><span>w mush</span><span>$16.5</span></div>
        <div class="r"><span>w leg ham</span><span>$16.5</span></div>
        <div class="r"><span>w bacon</span><span>$16.5</span></div>
        <div class="r"><span>w salmon</span><span>$18.5</span></div>
      </div></div>
    <div class="item"><div class="row"><span>The Big Thistle Breakfast Toasted</span><span class="price">$19.5</span></div>
      <div class="desc">sourdough, bacon, eggs, chorizo, tomato, mushrooms, baby spinach, hash brown w/ house relish</div></div>
    <div class="item"><div class="row"><span>French Toast</span><span class="price">$15.5</span></div>
      <div class="desc">brioche bread soaked in a creamy cinnamon mix, fried &amp; served with maple syrup, vanilla ice-cream &amp; berry compote</div></div>
    <div class="item"><div class="row"><span>Pancakes two stack of pancakes</span><span class="price">$12.5</span></div>
      <div class="desc lower">topped w maple syrup &amp; ice cream, add grilled banana +$2.0</div></div>
    <div class="item"><div class="row"><span>Breakfast Wrap Bacon</span><span class="price">$13.5</span></div>
      <div class="desc">fried egg, spinach, cheese topped with house made relish</div></div>
    <div class="item plain"><div class="row"><span>Croissants</span><span class="price"></span></div>
      <div class="mini" style="font-size:8px;text-transform:none">
        <div class="r"><span>ham, cheese &amp; tomato</span><span>$8.5</span></div>
        <div class="r"><span>ham, cheese &amp; avocado</span><span>$9.5</span></div>
      </div></div>
    <div class="extras">
      <div class="label">- - - Extra's / Sides - - -</div>
      <div>$4 each: bacon (2) - egg (2) - chorizo - salmon - mushrooms</div>
      <div>$2 each: grilled tomato - baby spinach (wilted) - avocado - hash brown</div>
      <div style="margin-top:4px">Most items can be made gluten free* (+$1.0) chorizo(gf), bacon(gf), ham(gf), relish(gf), hash browns (gf)</div>
    </div>
    <div class="vegan">Vegans - we are more than happy to make something to suit you</div>
  </div>

  <div class="col lunch">
    <header class="menu-head"><h2>Lunch Menu</h2><div class="when">Mon to Fri 7.30am<br>Sat &amp; Sun 11.30am</div></header>
    <div class="group-title">Wraps</div>
    <div class="group-note">lightly toasted &amp; served w/ beer battered chips</div>
    <div class="item"><div class="row"><span>Chicken</span><span class="price">$15.5</span></div>
      <div class="desc">w/ bacon, mixed lettuce, tasty cheese &amp; your choice of sauce (sweet chilli &amp; sour cream / caesar / aioli / ranch)</div></div>
    <div class="item"><div class="row"><span>Thistle</span><span class="price">$16.5</span></div>
      <div class="desc">mixed lettuce, sundried tomato, grilled bacon, crumbed chicken, tasty cheese &amp; aioli</div></div>
    <div class="item"><div class="row"><span>Vegie Wrap</span><span class="price">$15.5</span></div>
      <div class="desc">grilled mushrooms, capsicum, onion, tomato, fetta, spinach and a balsamic glaze</div></div>
    <div class="item"><div class="row"><span>Lentil Wrap</span><span class="price">$15.5</span></div>
      <div class="desc">our own lentil patty w/ lettuce, tomato, avocado, cheese, mango chutney &amp; sour cream</div></div>
    <div class="item"><div class="row"><span>Chicken Fajita</span><span class="price">$15.5</span></div>
      <div class="desc">seasoned chicken w/ capsicum, onion, our guacamole, cheese &amp; salsa served w a side of sour cream</div></div>
    <div class="item"><div class="row"><span>Beef Burrito</span><span class="price">$16.5</span></div>
      <div class="desc">seasoned pulled beef, brown rice, black beans, lettuce, cheese, guacamole, spicy salsa &amp; sour cream</div></div>
    <div class="item"><div class="row"><span>Vegie Wrap</span><span class="price">$15.5</span></div>
      <div class="desc">grilled mushrooms, capsicum, onion, tomato, fetta, spinach and a balsamic glaze</div></div>

    <div class="group-title">House Made Chicken Schnitzels</div>
    <div class="group-note">all schnitzels are prepared freshly in house, served w/ a side salad &amp; beer battered chips</div>
    <div class="item"><div class="row"><span>Housemade Schnitzel</span><span class="price">$18.5</span></div>
      <div class="desc">w/ your choice of mushroom, pepper or gravy</div></div>
    <div class="item"><div class="row"><span>Chicken &amp; Avocado</span><span class="price">$19.5</span></div>
      <div class="desc">schnitzel topped w/ fresh avocado &amp; cheese</div></div>
    <div class="item"><div class="row"><span>Parma</span><span class="price">$19.5</span></div>
      <div class="desc">schnitzel topped w/ our tomato sauce, ham &amp; grilled cheese</div></div>
    <div class="item"><div class="row"><span>Hawaiian</span><span class="price">$19.5</span></div>
      <div class="desc">schnitzel topped w/ leg ham, pineapple &amp; tasty cheese</div></div>

    <div class="group-title">Burgers</div>
    <div class="group-note">made on fresh toasted turkish bread &amp; served w/ beer battered chips</div>
    <div class="item"><div class="row"><span>B.L.A.T</span><span class="price">$14.5</span></div>
      <div class="desc">bacon, mixed lettuce, avocado &amp; fresh tomato, aioli</div></div>
    <div class="item"><div class="row"><span>Lentil Burger</span><span class="price">$15.5</span></div>
      <div class="desc">our own lentil patty, cheese, tomato, avocado, lettuce, mango chutney &amp; sour cream</div></div>
    <div class="item"><div class="row"><span>Schnitzel Burger</span><span class="price">$18.5</span></div>
      <div class="desc">house made schnitzel, grilled bacon, lettuce, tasty cheese w/ your choice of sweet chilli &amp; sour cream / caesar / aioli / ranch</div></div>
    <div class="item"><div class="row"><span>American Burger</span><span class="price">$16.5</span></div>
      <div class="desc">150g house made patty w/ cheese, tomato, lettuce, pickles, tomato ketchup, mustard &amp; mayo</div></div>
    <div class="item plain"><div class="row"><span>Grilled Chicken Burger</span><span class="price">$16.5</span></div>
      <div class="desc">char grilled chicken breast, cheese, avocado, tomato, lettuce &amp; your choice of sauce (sweet chilli &amp; sour cream / caesar / aioli / ranch)</div></div>
  </div>
</section>

</body>
</html>
```